Drillvane Business Card Design Project

We need a business card design for a new company called "Drillvane Systems". Drillvane provides 3D visualization software for subsurface oil and gas data so you can make confident downhole decisions.

Our goal is to provide easy to understand big pictures of your data so your can make confident planning decisions.

Our tagline is
SEAMLESS DATA SHARING. EFFECTIVE COLLABORATION. CONFIDENT DECISION-MAKING

Check out http://www.drillvane-example.com for more ideas.

The design should promote a technology company that delivers web-based solutions focused on photo-realistic 3D graphics.

The colors from our existing logo (attached) are one option but not a requirement. The design SHOULD NOT use the existing logo.

The design should be two sided and full color. If you require any special print considerations (example: paper type, matte finish, metallic ink, etc) please provide detailed comments. Please also specify any desired details such as rounding of corners, etc.

IF YOU USE BLACK our printer states "We recommend using CMYK black (0, 0, 0, 100) or for a rich black (60, 40, 40, 100). Ensure your artwork is in CMYK mode before adjusting the black."

For design purposes you can use the following contact information

name: Marcus Pell
title: founder
phone: 555.987.6543
email: marcus@drillvane-example.com

company information
Drillvane is our "branded" name
"Drillvane Systems" is our official name
www.drillvane-example.com

address:
Suite 210
482 Larkin Avenue SW
Calgary, AB, Canada
T3K 4R8

Target Market(s)

Companies spend a lot of time collecting, organizing and analyzing data but it's really hard to to get a big picture view of current and planned projects, especially in context to existing wellbores, geology and downhole equipment

Drillvane enables you to explore the big picture in an immersive, 3D environment. Our goal is to help transform you rich data into an easily understood picture, to make confident planning decisions and anticipate trouble events before the expensive execution phase.

Industry/Entity Type

Oil And Gas

Requirements
Must have
• The business card design should be sized to a standard 3.5 x 2 inches and print ready. See the attachment for a sample sized card
It MUST meet these requirements:
Exported as PDF file with two pages:
page 1: front design
page 2: back design
All Images must be 300ppi or higher (at 100%)
CMYK colour mode
0.125 inches of bleed on all sides (0.25 inches additional width and height)
0.125 inch safety margin (inside trim line)

```html
<!DOCTYPE html>
<html lang="en">
<head>
<meta charset="utf-8">
<title>Drillvane Business Card</title>
<link rel="stylesheet" href="https://fonts.googleapis.com/css2?family=Questrial&family=Arimo:wght@400&display=swap">
<style>
  :root {
    --backdrop: #dcdcdc;
    --card-dark: #242424;
    --card-light: #ffffff;
    --brand-green: #8dc63f;
    --ink: #2a2a2a;
    --white: #ffffff;
  }
  * { margin: 0; padding: 0; box-sizing: border-box; }
  html, body { width: 1200px; height: 840px; overflow: hidden; }
  body { background: var(--backdrop); position: relative; font-family: "Arimo", Arial, sans-serif; }

  .card { position: absolute; top: 275px; width: 466px; height: 265px; overflow: hidden; }
  .card-front { left: 87px; background: var(--card-dark); }
  .card-back { left: 648px; background: var(--card-light); }

  .front-brand {
    position: absolute; left: 0; right: 0; top: 0; bottom: 0;
    display: flex; align-items: center; justify-content: center; gap: 16px;
  }
  .front-brand .brand-mark { width: 34px; height: 34px; background: var(--brand-green); }
  .front-brand .brand-name {
    font-family: "Questrial", sans-serif; font-size: 52px; color: var(--white); letter-spacing: -0.5px;
  }

  .back-brand {
    position: absolute; left: 22px; top: 52px; display: flex; align-items: center; gap: 10px;
  }
  .back-brand .brand-mark { width: 22px; height: 22px; background: var(--brand-green); }
  .back-brand .brand-name {
    font-family: "Questrial", sans-serif; font-size: 33px; color: var(--brand-green);
  }

  .name-tab {
    position: absolute; left: -6px; top: 164px; width: 12px; height: 30px;
    border-radius: 6px; background: var(--brand-green);
  }
  .person { position: absolute; left: 21px; top: 161px; }
  .person-name { font-size: 18px; color: var(--ink); line-height: 1.1; }
  .person-title { font-size: 13px; color: var(--brand-green); margin-top: 2px; }

  .contacts { position: absolute; left: 280px; top: 161px; list-style: none; }
  .contacts li {
    display: flex; align-items: center; gap: 9px; height: 19px;
    font-size: 13px; color: var(--ink);
  }
  .contacts svg { width: 15px; height: 15px; fill: var(--brand-green); flex: none; }

  .footer-bands { position: absolute; left: 0; bottom: 0; width: 466px; height: 30px; }
  .footer-url {
    position: absolute; left: 300px; bottom: 8px; font-size: 13px; color: var(--white);
  }
</style>
</head>
<body>

  <section class="card card-front" aria-label="Card front">
    <div class="front-brand">
      <span class="brand-mark"></span>
      <span class="brand-name">Drillvane</span>
    </div>
  </section>

  <section class="card card-back" aria-label="Card back">
    <div class="back-brand">
      <span class="brand-mark"></span>
      <span class="brand-name">Drillvane</span>
    </div>

    <span class="name-tab"></span>
    <div class="person">
      <p class="person-name">Marcus Pell</p>
      <p class="person-title">President</p>
    </div>

    <ul class="contacts">
      <li>
        <svg viewBox="0 0 16 16" aria-hidden="true"><path d="M3.2 1.5l2.3 2.6-1.3 1.8c.9 2 2.4 3.6 4.4 4.6l1.8-1.3 2.6 2.3-1.6 2.4C6 13.4 2.5 9.8 1 4.3z"/></svg>
        <span>555 987 6543</span>
      </li>
      <li>
        <svg viewBox="0 0 16 16" aria-hidden="true"><path d="M4 1h8v4H4z M1 6h14v6h-3v3H4v-3H1z M5 10v4h6v-4z" fill-rule="evenodd"/></svg>
        <span>555 987 6544</span>
      </li>
      <li>
        <svg viewBox="0 0 16 16" aria-hidden="true"><circle cx="8" cy="8" r="7"/><path d="M5 4c2 0 2 2 1 3s1 3-1 4M10 3c-1 2 1 3 2 2M11 10c-1 0-2 1-1 3" stroke="#fff" stroke-width="1.3" fill="none"/></svg>
        <span>marcus@drillvane-example.com</span>
      </li>
    </ul>

    <svg class="footer-bands" viewBox="0 0 466 30" aria-hidden="true">
      <polygon points="0,7 268,7 261,15 0,15" fill="var(--brand-green)"/>
      <polygon points="0,19 259,19 273,2 466,2 466,30 0,30" fill="var(--card-dark)"/>
    </svg>
    <p class="footer-url">www.drillvane-example.com</p>
  </section>

</body>
</html>
```